Stationary (Business Cards, envelopes, cover letters, etc) for HARBOR LANTERN PARTNERS
The Harbor Lantern Partners
Stationary (Business Cards, envelopes, cover letters, etc) for HARBOR LANTERN PARTNERS - Business Opportunities
Creative Brief
Professional
Rodrigo Velasco Brennan
Av. Ignacio Marroquín 718 B Col. Los Pinos Altos México DF CP 01482 México
rvelasco@hlp-example.mx
www.hlp-example.mx
First impressions have high impact, so in terms of the business card, it has to be something that's out of the box. The card is used to present ourselves to another party or prospect, but it also has to have a high impact message, either by an image or a phrase that comes attached in the back side. It could be some key points of a preview success case. So the back side has to have a marketing application. It has to be a card that will stand out, so much that it will be shown and passed around. In design and in materials (maybe???), although win the materials it will have a high impact on the costs of production. It has to be standard size, so it fits in every wallet thus avoiding on being thrown somewhere.
Concepts
Business Card and Stationary Project for a multifaceted corporation
Stationary for holding company
Business cards for RFTV - Investimentos e Administrações
mitiha mitiha
GREAT NEWS! WE'VE EXTENDED TO THIS FRIDAY! KEEP UP THE GREAT WORK!!!
Hi designers! GREAT JOB! We are want to decide today (our time) the winner. Please if you have any questions, let us know. Try to show as much applications as possible, i.e. we're now in a digital world so some digital applications we'll be considered for higher points. Have seen proposals in blue and gray (predominant colors and mixed), but none in orange. Let's see some! *Don't use curved lines in your design proposals. THANKS!
Hi, first of all I want to thank each and every one of you for accepting in working on our project. GREAT DESIGNS !!!!! Something we don't want is the lines that make a "curve" to separate content. I've seen a lot of those in the market and we want to be ORIGINAL. As I said in the brief, we want our cards to be saved as something awsome, and to be shown to other people. Material: sent your proposals of other materials, however if you can also send the specificatiosn of that material so we can see the cost of printing in them. Remember that it's not only the business cards but the stationary. KEEP UP THE GREAT JOB! CREATE DESIGN!

```html
<!DOCTYPE html>
<html lang="en">
<head>
<meta charset="utf-8">
<title>The Harbor Lantern Partners – Business Cards</title>
<link rel="stylesheet" href="https://fonts.googleapis.com/css2?family=Open+Sans:wght@400;600;700&display=swap">
<style>
  :root {
    --backdrop: #1d1d1f;
    --card-white: #ffffff;
    --card-dark: #2b2b2d;
    --band-grey: #8c8c8e;
    --band-light: #d9d9db;
    --ink-dark: #2a2a2c;
    --ink-muted: #6b6b6e;
    --ink-light: #f2f2f2;
    --brand-blue: #2f8fcf;
  }
  * { box-sizing: border-box; margin: 0; padding: 0; }
  html, body {
    width: 1200px; height: 646px; overflow: hidden;
    background: var(--backdrop);
    font-family: "Open Sans", Arial, sans-serif;
  }
  .card-stage { position: relative; width: 1200px; height: 646px; }
  .card {
    position: absolute; top: 180px;
    width: 500px; height: 286px;
    border-radius: 16px; overflow: hidden;
    background: var(--card-white);
  }
  .card--front { left: 70px; }
  .card--back { left: 630px; }

  .brand { display: flex; align-items: center; gap: 10px; }
  .brand__mark { width: 22px; height: 22px; background: var(--brand-blue); flex: none; }
  .brand__name {
    font-size: 15px; font-weight: 600; color: var(--ink-dark);
    letter-spacing: 0.5px; white-space: nowrap;
  }

  .front-lockup {
    position: absolute; left: 50%; top: 50%;
    transform: translate(-50%, -50%);
    display: flex; flex-direction: column; align-items: center; gap: 10px;
  }
  .front-lockup__message {
    font-size: 10px; color: var(--ink-muted);
    letter-spacing: 1.5px; text-transform: uppercase; white-space: nowrap;
  }

  .card__bands { position: absolute; inset: 0; }

  .card--back .brand { position: absolute; left: 40px; top: 110px; gap: 8px; }
  .card--back .brand__mark { width: 16px; height: 16px; }
  .card--back .brand__name { font-size: 11px; }

  .holder { position: absolute; right: 22px; top: 18px; text-align: right; }
  .holder__name { font-size: 14px; font-weight: 700; color: var(--ink-dark); }
  .holder__role { font-size: 11px; color: var(--ink-muted); }

  .phones {
    position: absolute; right: 22px; top: 152px; text-align: right;
    font-size: 9.5px; line-height: 1.6; color: var(--ink-light);
  }
  .contact {
    position: absolute; left: 22px; bottom: 22px;
    font-size: 9.5px; line-height: 1.6; color: var(--ink-light);
  }
</style>
</head>
<body>
<main class="card-stage">
  <section class="card card--front" aria-label="Business card front">
    <div class="front-lockup">
      <div class="brand">
        <span class="brand__mark"></span>
        <span class="brand__name">The Harbor Lantern Partners</span>
      </div>
      <p class="front-lockup__message">Opening doors to new markets</p>
    </div>
  </section>

  <section class="card card--back" aria-label="Business card back">
    <svg class="card__bands" viewBox="0 0 500 286" preserveAspectRatio="none" aria-hidden="true">
      <polygon points="0,170 330,156 500,62 500,286 0,286" fill="var(--band-light)"/>
      <polygon points="0,180 335,166 500,78 500,286 0,286" fill="var(--band-grey)"/>
      <polygon points="0,190 340,176 500,94 500,286 0,286" fill="var(--card-dark)"/>
    </svg>
    <div class="holder">
      <p class="holder__name">Marisol Quevedo Lange</p>
      <p class="holder__role">Consultant</p>
    </div>
    <div class="brand">
      <span class="brand__mark"></span>
      <span class="brand__name">The Harbor Lantern Partners</span>
    </div>
    <div class="phones">
      <p>P : 055 218 4470</p>
      <p>F : 055 218 4471</p>
    </div>
    <div class="contact">
      <p>mquevedo@hlp-example.mx</p>
      <p>www.hlp-example.mx</p>
      <p>Av. Ignacio Marroquín 718 B, Los Pinos</p>
    </div>
  </section>
</main>
</body>
</html>
```